POLITICAL CARD TO HAND OUT

A LITTLE LARGER THAN THE REGULAR BUSINESS CARD WITH THE ABOVE INFORMATION.

Industry/Entity Type

Business

Contact Information for Business Card

ELECT *RAY DUNNER* FOR JUSTICE OF THE PEACE PCT 6-EXPERIENCED LEADERSHIP- WITH MY PICTURE ON IT- PHONE 555-318-2760-REPUBLICAN PRIMARY - EARLY VOTING FEB 18TH THRU FEB 28 AND ELECTION DAY IS MARCH 4TH, 2014- USE RED WHITE AND BLUE WITH SOME STARS.

Requirements
Must have
• A FIVE POINTED STAR ON EACH SIDE OF MY NAME

```html
<!DOCTYPE html>
<html lang="en">
<head>
<meta charset="utf-8">
<title>Ray Dunner – Justice of the Peace Card</title>
<link rel="stylesheet" href="https://fonts.googleapis.com/css2?family=Lato:wght@400;700&display=swap">
<style>
  :root {
    --backdrop: #d9d9d9;
    --card-white: #f7f7f7;
    --flag-red: #b51f2a;
    --flag-blue: #173f73;
    --text-light: #ffffff;
    --text-dark: #2c2c2c;
    --portrait-tone-a: #c9b9a6;
    --portrait-tone-b: #3a3030;
  }
  html, body {
    margin: 0;
    padding: 0;
    width: 1200px;
    height: 750px;
    overflow: hidden;
    background: var(--backdrop);
  }
  .canvas {
    position: relative;
    width: 1200px;
    height: 750px;
    display: flex;
    align-items: center;
    justify-content: center;
  }
  .campaign-card {
    position: relative;
    width: 960px;
    height: 560px;
    border-radius: 44px;
    overflow: hidden;
    background: var(--card-white);
    box-shadow: 0 10px 30px rgba(0,0,0,0.18);
    font-family: "Lato", sans-serif;
  }
  .card-bands {
    position: absolute;
    inset: 0;
  }
  .portrait {
    position: absolute;
    left: 45px;
    top: 190px;
    width: 210px;
    height: 210px;
    border-radius: 50%;
    background: radial-gradient(circle at 50% 40%, var(--portrait-tone-a) 0%, #9c7f6a 45%, var(--portrait-tone-b) 100%);
  }
  .headline {
    position: absolute;
    left: 290px;
    top: 58px;
    padding-left: 14px;
    border-left: 2px solid var(--text-light);
    color: var(--text-light);
  }
  .star-row {
    display: flex;
    gap: 5px;
    margin-bottom: 8px;
  }
  .star-row svg { width: 16px; height: 16px; fill: var(--text-light); }
  .headline-text {
    margin: 0;
    font-size: 22px;
    line-height: 28px;
    font-weight: 400;
    text-transform: uppercase;
    letter-spacing: 0.3px;
    white-space: nowrap;
  }
  .name-star {
    display: inline-block;
    width: 15px;
    height: 15px;
    margin: 0 4px;
    vertical-align: 1px;
    fill: var(--text-light);
  }
  .voting-info {
    position: absolute;
    left: 300px;
    top: 345px;
    margin: 0;
    color: var(--text-dark);
    font-size: 27px;
    line-height: 34px;
    font-weight: 400;
    text-transform: uppercase;
  }
</style>
</head>
<body>
<main class="canvas">
  <article class="campaign-card">
    <svg class="card-bands" width="960" height="560" viewBox="0 0 960 560" aria-hidden="true">
      <polygon points="0,0 960,0 960,40 520,248 0,340" fill="var(--flag-red)"/>
      <polygon points="520,248 960,40 960,170" fill="var(--flag-blue)"/>
    </svg>

    <div class="portrait" role="img" aria-label="Portrait photo of the candidate in a cowboy hat and suit"></div>

    <header class="headline">
      <div class="star-row" aria-hidden="true">
        <svg viewBox="0 0 24 24"><polygon points="12,1 15,9 23,9 16.5,14 19,22 12,17 5,22 7.5,14 1,9 9,9"/></svg>
        <svg viewBox="0 0 24 24"><polygon points="12,1 15,9 23,9 16.5,14 19,22 12,17 5,22 7.5,14 1,9 9,9"/></svg>
        <svg viewBox="0 0 24 24"><polygon points="12,1 15,9 23,9 16.5,14 19,22 12,17 5,22 7.5,14 1,9 9,9"/></svg>
        <svg viewBox="0 0 24 24"><polygon points="12,1 15,9 23,9 16.5,14 19,22 12,17 5,22 7.5,14 1,9 9,9"/></svg>
        <svg viewBox="0 0 24 24"><polygon points="12,1 15,9 23,9 16.5,14 19,22 12,17 5,22 7.5,14 1,9 9,9"/></svg>
      </div>
      <h1 class="headline-text">Elect<svg class="name-star" viewBox="0 0 24 24" aria-hidden="true"><polygon points="12,1 15,9 23,9 16.5,14 19,22 12,17 5,22 7.5,14 1,9 9,9"/></svg>Ray Dunner<svg class="name-star" viewBox="0 0 24 24" aria-hidden="true"><polygon points="12,1 15,9 23,9 16.5,14 19,22 12,17 5,22 7.5,14 1,9 9,9"/></svg>for Justice of<br>the Peace Pct 6-Experienced<br>Leadership</h1>
    </header>

    <p class="voting-info">
      Phone 555-318-2760-Republican Primary-<br>
      Early Voting Feb 18th thru Feb 28<br>
      Election Day is March 4th, 2014
    </p>
  </article>
</main>
</body>
</html>
```